We are an integrated facilities management company.

We aggregate everything related to facilities maintenance. Repair-replacement of equipment and facility space materials from:
Asset gathering and tracking.
Vendor screening, contracting and management.
Service requirement development.
Work order processing and management.
Invoice reconciliation.
Vendor payment.
Reporting.
Capital equipment bids and project management.

Target Market(s)

Retail, hospitality, multi-family housing, long term healthcare.

Industry/Entity Type

Maintenance

Contact Information for Business Card

Professional and bold look. (see logo zip file)

Colors
3377b5
85abd2
cedeed

Requirements
Must have
• N/A
Nice to have
• N/A
Should not have
• N/A

```html
<!DOCTYPE html>
<html lang="en">
<head>
<meta charset="utf-8">
<title>Keystone Facility Partners – Business Card</title>
<link rel="stylesheet" href="https://fonts.googleapis.com/css2?family=Libre+Baskerville:wght@700&family=Raleway:wght@500;600;700&display=swap">
<style>
  :root {
    --backdrop: #d3d3d3;
    --card-white: #ffffff;
    --brand-blue: #2a77b8;
    --brand-deep: #2a6fad;
    --brand-light: #85abd2;
    --brand-pale: #cedeed;
    --slate: #3f5b72;
    --slate-on-blue: #3a5f80;
    --ink: #333a40;
  }
  * { margin: 0; padding: 0; box-sizing: border-box; }
  html, body {
    width: 1125px;
    height: 1200px;
    overflow: hidden;
    background: var(--backdrop);
  }
  .sheet {
    position: relative;
    width: 1125px;
    height: 1200px;
  }
  .card {
    position: absolute;
    left: 178px;
    width: 768px;
    height: 437px;
    border-radius: 24px;
    overflow: hidden;
  }
  .card--front { top: 140px; background: var(--card-white); }
  .card--back  { top: 626px; background: var(--brand-blue); }

  .brand {
    position: absolute;
    display: flex;
    align-items: center;
    gap: 10px;
    font-family: "Raleway", sans-serif;
    font-weight: 700;
    white-space: nowrap;
  }
  .brand__mark { display: block; flex: none; }
  .card--front .brand {
    left: 62px;
    top: 198px;
    font-size: 19px;
    color: var(--slate);
  }
  .card--front .brand__mark { width: 16px; height: 16px; background: var(--slate); }
  .card--back .brand {
    left: 50%;
    top: 50%;
    transform: translate(-50%, -50%);
    font-size: 32px;
    color: var(--slate-on-blue);
    gap: 14px;
  }
  .card--back .brand__mark { width: 26px; height: 26px; background: var(--slate-on-blue); }

  .divider {
    position: absolute;
    left: 384px;
    top: 108px;
    width: 2px;
    height: 221px;
    background: var(--brand-light);
  }
  .details {
    position: absolute;
    left: 402px;
    top: 108px;
    font-family: "Raleway", sans-serif;
    color: var(--ink);
  }
  .person-name {
    font-family: "Libre Baskerville", serif;
    font-weight: 700;
    font-size: 23px;
    letter-spacing: 1.5px;
    line-height: 32px;
    color: var(--brand-deep);
  }
  .person-name__last { color: var(--brand-light); }
  .person-role {
    font-weight: 600;
    font-size: 18px;
    line-height: 24px;
    margin-top: 2px;
  }
  .address {
    font-style: normal;
    font-weight: 500;
    font-size: 17.5px;
    line-height: 22px;
    margin-top: 16px;
  }
  .contacts { list-style: none; margin-top: 18px; }
  .contacts__item {
    display: flex;
    align-items: center;
    gap: 9px;
    font-weight: 500;
    font-size: 18px;
    line-height: 22px;
    margin-bottom: 8.5px;
  }
  .contacts__icon { width: 13px; height: 13px; flex: none; }
  .web__domain { color: var(--brand-light); }
</style>
</head>
<body>
<main class="sheet">
  <section class="card card--front" aria-label="Card front">
    <div class="brand"><span class="brand__mark"></span>Keystone Facility Partners</div>
    <div class="divider"></div>
    <div class="details">
      <h1 class="person-name">Marta <span class="person-name__last">Lindqvist</span></h1>
      <p class="person-role">Doctor</p>
      <address class="address">1800 Harbor Row<br>Glen Arden, Maryland 20730</address>
      <ul class="contacts">
        <li class="contacts__item">
          <svg class="contacts__icon" viewBox="0 0 16 16" aria-hidden="true"><path fill="#2a77b8" d="M3.5 1 6 3.6 4.6 5.4c.8 2 2.3 3.5 4.1 4.4l1.8-1.4L13 11l-1.6 2.6C6.4 13.2 2.6 9.3 1.5 4.3z"/><path fill="none" stroke="#2a77b8" stroke-width="1.2" d="M9.5 2.5a4 4 0 0 1 4 4M9.5 5a1.6 1.6 0 0 1 1.6 1.6"/></svg>
          <span>410-555-0148</span>
        </li>
        <li class="contacts__item">
          <svg class="contacts__icon" viewBox="0 0 16 16" aria-hidden="true"><rect x="1" y="3" width="14" height="10" rx="1" fill="#2a77b8"/><path d="M3 5.5 8 9l5-3.5" fill="none" stroke="#fff" stroke-width="1.4"/></svg>
          <span>info@keystonefp.com</span>
        </li>
        <li class="contacts__item">
          <svg class="contacts__icon" viewBox="0 0 16 16" aria-hidden="true"><circle cx="8" cy="8" r="7" fill="#2a77b8"/><path fill="#fff" d="M4 4.5c1.5.2 2.3 1 2.2 2.3-.9.4-1.6 1.2-1.4 2.5L3.3 9.6C2.6 7.6 2.9 5.8 4 4.5zM9.3 2.4c.8.7 1.6 1.8 1 2.8-.6.7-1.6.6-1.8 1.5.6 1 2 .9 2.5 2-.4 1.7-1.4 3.2-2.6 4.2 2.7-.4 4.4-2.5 4.6-5.1C13 5 11.6 3 9.3 2.4z"/></svg>
          <span>www.<span class="web__domain">keystonefp</span>.com</span>
        </li>
      </ul>
    </div>
  </section>

  <section class="card card--back" aria-label="Card back">
    <div class="brand"><span class="brand__mark"></span>Keystone Facility Partners</div>
  </section>
</main>
</body>
</html>
```